High-End Executive Transportation

We need a business card to represent our high-end executive transportation company called KORVEL Transportation. We would like designs for rectangular and square cards with rounded corners. We want the card to incorporate a QR code, www.korveltransportation.example on the back. The attached picture shows a picture of our vehicle and we would like the card to match the two-tone paint scheme with silver being on top and black being on the bottom. We want the card to be simple, but represent high-end.

The card needs to have a line for employee name, office and cell phone number, email address, and website.

```html
<!DOCTYPE html>
<html lang="en">
<head>
<meta charset="utf-8">
<title>KORVEL Transportation – Business Card</title>
<link href="https://fonts.googleapis.com/css2?family=Work+Sans:wght@400;500;600&display=swap" rel="stylesheet">
<style>
  :root {
    --page: #fbfcfd;
    --card-black: #060808;
    --silver-light: #f7f6f2;
    --silver-mid: #ebe6dc;
    --silver-cool: #d3d6dd;
    --silver-text: #e8e6e1;
    --ink: #111111;
    --shadow: rgba(0, 0, 0, 0.35);
  }
  * { margin: 0; padding: 0; box-sizing: border-box; }
  html, body {
    width: 1200px; height: 900px; overflow: hidden;
    background: var(--page);
    font-family: "Work Sans", Arial, sans-serif;
  }
  .canvas { position: relative; width: 1200px; height: 900px; }

  .card {
    position: absolute; width: 632px; height: 362px;
    background: var(--card-black);
    border-radius: 14px;
    box-shadow: 10px 10px 14px var(--shadow);
    overflow: hidden;
  }
  .card--front { left: 128px; top: 64px; }
  .card--back { left: 440px; top: 475px; }

  .silver-fill {
    background: linear-gradient(90deg, var(--silver-cool) 0%, var(--silver-light) 22%, var(--silver-mid) 45%, var(--silver-light) 70%, var(--silver-mid) 88%, var(--silver-cool) 100%);
  }

  /* Front */
  .wordmark {
    position: absolute; left: 0; right: 0; top: 96px;
    text-align: center; color: var(--silver-text); font-weight: 600;
  }
  .wordmark__name { display: block; font-size: 74px; line-height: 1; letter-spacing: 2px; }
  .wordmark__sub { display: block; font-size: 30px; line-height: 1.4; margin-top: 6px; }
  .front-url {
    position: absolute; left: 0; right: 0; top: 296px;
    text-align: center; color: var(--silver-text);
    font-size: 15px; line-height: 20px; letter-spacing: 4px;
  }
  .front-band { position: absolute; left: 0; right: 0; bottom: 0; height: 23px; }

  /* Back */
  .info-bar {
    position: absolute; left: 0; height: 45px;
    display: flex; align-items: center;
    color: var(--ink); font-size: 16px; white-space: nowrap;
  }
  .info-bar--name { top: 54px; width: 307px; clip-path: polygon(0 0, 298px 0, 307px 100%, 0 100%); padding-left: 24px; }
  .info-bar--office { top: 114px; width: 318px; clip-path: polygon(0 0, 310px 0, 318px 100%, 0 100%); }
  .info-bar--cell { top: 175px; width: 330px; clip-path: polygon(0 0, 322px 0, 330px 100%, 0 100%); }
  .info-bar--web { top: 235px; width: 342px; clip-path: polygon(0 0, 334px 0, 342px 100%, 0 100%); }
  .info-bar--mail { top: 295px; width: 354px; clip-path: polygon(0 0, 346px 0, 354px 100%, 0 100%); }
  .info-bar__icon { width: 18px; height: 18px; margin-left: 20px; margin-right: 20px; flex: none; }

  .back-wordmark {
    position: absolute; left: 371px; top: 52px;
    color: var(--silver-text); font-weight: 600;
  }
  .back-wordmark__name { display: block; font-size: 46px; line-height: 1; letter-spacing: 1px; }
  .back-wordmark__sub { display: block; font-size: 20px; line-height: 1.4; margin-top: 4px; }
  .address {
    position: absolute; left: 394px; top: 178px;
    color: var(--silver-text); font-size: 16px; line-height: 20px; font-style: normal;
  }
  .qr-area {
    position: absolute; left: 394px; top: 238px;
    width: 92px; height: 92px;
    background: var(--silver-light);
    border-radius: 6px;
  }
</style>
</head>
<body>
<main class="canvas">

  <section class="card card--front" aria-label="Card front">
    <div class="wordmark">
      <span class="wordmark__name">KORVEL</span>
      <span class="wordmark__sub">Transportation</span>
    </div>
    <p class="front-url">www.korveltransportation.example</p>
    <div class="front-band silver-fill"></div>
  </section>

  <section class="card card--back" aria-label="Card back">
    <div class="info-bar info-bar--name silver-fill">Employee name</div>

    <div class="info-bar info-bar--office silver-fill">
      <svg class="info-bar__icon" viewBox="0 0 24 24" fill="none" stroke="#111" stroke-width="2" stroke-linecap="round" stroke-linejoin="round" aria-hidden="true">
        <path d="M5 3h4l2 5-3 2a11 11 0 0 0 6 6l2-3 5 2v4a2 2 0 0 1-2 2A17 17 0 0 1 3 5a2 2 0 0 1 2-2z"/>
        <path d="M15 3a6 6 0 0 1 6 6M15 7a2 2 0 0 1 2 2"/>
      </svg>
      012 555 0142
    </div>

    <div class="info-bar info-bar--cell silver-fill">
      <svg class="info-bar__icon" viewBox="0 0 24 24" fill="none" stroke="#111" stroke-width="2" aria-hidden="true">
        <rect x="6" y="2" width="12" height="20" rx="2"/>
        <line x1="10" y1="18" x2="14" y2="18"/>
      </svg>
      012 555 0143
    </div>

    <div class="info-bar info-bar--web silver-fill">
      <svg class="info-bar__icon" viewBox="0 0 24 24" fill="none" stroke="#111" stroke-width="2" aria-hidden="true">
        <circle cx="12" cy="12" r="10"/>
        <ellipse cx="12" cy="12" rx="4" ry="10"/>
        <line x1="2" y1="12" x2="22" y2="12"/>
        <line x1="12" y1="2" x2="12" y2="22"/>
      </svg>
      www.korveltransportation.example
    </div>

    <div class="info-bar info-bar--mail silver-fill">
      <svg class="info-bar__icon" viewBox="0 0 24 24" fill="none" stroke="#111" stroke-width="2" aria-hidden="true">
        <rect x="2" y="5" width="20" height="14"/>
        <path d="M2 5l10 8 10-8M2 19l8-7M22 19l-8-7"/>
      </svg>
      office@korvel.example
    </div>

    <div class="back-wordmark">
      <span class="back-wordmark__name">KORVEL</span>
      <span class="back-wordmark__sub">Transportation</span>
    </div>

    <address class="address">1234 Korvel Road<br>Korvel City, CA 1234</address>

    <div class="qr-area" role="img" aria-label="QR code linking to the company website"></div>
  </section>

</main>
</body>
</html>
```